yourSmile Kelvin Grove Business Card

Please design a two sided business card that is Elegant and Professional
Add subtle elegant patterns to suit Spot UV printing/ or raised printing

Name: Dr Marcus L. Avery
Qualification: BDSc (QLD)
Title: Dental Surgeon, Clinical Director
Company: yourSmile Kelvin Grove
Phone: (02) 9376 2258
Address: Shop 5/12-14 Langford Rd Kelvin Grove 2117
email: info@yoursmilekelvingrove.example.au
Facebook: facebook.com/yoursmilekelvingrove

Motto:
Quality dentistry you can trust

Description of services (not compulsory):
Preventative Dentistry | General Dentistry
Cosmetic Dentistry | Teeth Whitening
Crown and Bridge | Root Canal Therapy
Veneers | Clearbrace | Orthodontics
Emergency Dental Care | After Hours

Personalised Treatment Plans
Transparent Fees

Please make sure card is elegant and professional

Target Market(s)

general population, patients,
Dental sales companies, other professions

Industry/Entity Type

Dental Clinic

Contact Information for Business Card

Name: Dr Marcus L. Avery
Qualification: BDSc (QLD)
Phone: (02) 9376 2258
Address: Shop 5/12-14 Langford Rd Kelvin Grove

Motto:

Description of services (not compulsory)

Transparent Fees

Image of dental surgery optional

Please make sure card is elegant and profession

Requirements
Must have
• Logo
• Name, Title (next to name), Business
• Phone, address, facbeook
• Must have stylish design to suit SPOT UV reflective printing
Nice to have
• Subtle elegant patterns which will have Spot UV on them when printed
• Colours to match logo colour
• Description of services
Should not have
• Small fonts that are hard to read
• DO NOT PUT IMAGES OF DENTAL INSTRUMENTS OR TEETH PLEASE

```html
<!DOCTYPE html>
<html lang="en">
<head>
<meta charset="utf-8">
<title>yourSmile Kelvin Grove Business Card</title>
<link rel="stylesheet" href="https://fonts.googleapis.com/css2?family=Open+Sans:wght@400;600;700&display=swap">
<style>
  :root {
    --green: #7dbb2e;
    --green-dark: #62a21c;
    --grey: #8a8a8a;
    --charcoal: #5a5a5a;
    --charcoal-deep: #3e3e3e;
    --white: #ffffff;
    --backdrop: #ecebe8;
  }
  * { margin: 0; padding: 0; box-sizing: border-box; }
  html, body { width: 1200px; height: 950px; overflow: hidden; }
  body {
    background: var(--backdrop);
    font-family: "Open Sans", Arial, sans-serif;
    position: relative;
  }
  .card {
    position: absolute;
    left: 240px;
    width: 720px;
    height: 400px;
    border-radius: 4px;
    overflow: hidden;
    box-shadow: 0 10px 28px rgba(0,0,0,0.18);
  }

  /* Back side */
  .card-back {
    top: 50px;
    background: linear-gradient(135deg, var(--charcoal) 0%, var(--charcoal-deep) 100%);
    color: var(--white);
    text-align: center;
  }
  .back-brand {
    margin-top: 92px;
    font-size: 40px;
    font-weight: 600;
    color: rgba(255,255,255,0.9);
  }
  .back-motto {
    margin-top: 26px;
    font-size: 20px;
  }
  .services {
    margin-top: 16px;
    list-style: none;
    font-size: 15.5px;
    line-height: 1.7;
    color: rgba(255,255,255,0.88);
  }

  /* Front side */
  .card-front {
    top: 500px;
    background: var(--white);
  }
  .front-wave { position: absolute; inset: 0; }
  .brand {
    position: absolute;
    left: 58px;
    top: 62px;
    display: flex;
    align-items: center;
    gap: 14px;
  }
  .brand-dot {
    width: 22px; height: 22px;
    border-radius: 50%;
    background: var(--grey);
  }
  .brand-name {
    font-size: 38px;
    font-weight: 600;
    color: var(--green);
    line-height: 1.05;
  }
  .person {
    position: absolute;
    left: 34px;
    top: 262px;
    color: var(--white);
  }
  .person-name { font-size: 22px; font-weight: 700; }
  .person-qual { font-size: 15px; font-weight: 600; }
  .person-title { margin-top: 4px; font-size: 17px; }
  .contact {
    position: absolute;
    right: 28px;
    top: 222px;
    list-style: none;
    text-align: right;
    color: var(--white);
    font-size: 14.5px;
    line-height: 1.55;
  }
  .contact li { display: flex; justify-content: flex-end; align-items: center; gap: 8px; }
  .contact svg { width: 16px; height: 16px; flex: none; }
  .contact .social-box { width: 14px; height: 14px; background: var(--white); border-radius: 2px; flex: none; margin-right: 1px; }
  .contact .address { padding-right: 24px; }
  .contact .motto { margin-top: 2px; font-size: 15.5px; }
</style>
</head>
<body>

<section class="card card-back" aria-label="Business card back">
  <p class="back-brand">yourSmile Kelvin Grove</p>
  <p class="back-motto">Quality dentistry you can trust</p>
  <ul class="services">
    <li>Preventative Dentistry | General Dentistry | Cosmetic Dentistry</li>
    <li>Teeth Whitening | Crown and Bridge | Root Canal Therapy | Veneers</li>
    <li>Clearbrace | Orthodontics | Emergency Dental Care | After Hours</li>
    <li>Personalised Treatment Plans | Transparent Fees</li>
  </ul>
</section>

<section class="card card-front" aria-label="Business card front">
  <svg class="front-wave" width="720" height="400" viewBox="0 0 720 400" aria-hidden="true">
    <defs>
      <linearGradient id="greenBand" x1="0" y1="0" x2="0" y2="1">
        <stop offset="0" stop-color="#86c437"/>
        <stop offset="1" stop-color="#6aab22"/>
      </linearGradient>
    </defs>
    <path d="M0,188 C180,236 430,232 720,150" fill="none" stroke="#9a9a9a" stroke-width="7"/>
    <path d="M0,205 C190,250 440,244 720,164 L720,400 L0,400 Z" fill="url(#greenBand)"/>
  </svg>

  <div class="brand">
    <span class="brand-dot"></span>
    <span class="brand-name">yourSmile<br>Kelvin Grove</span>
  </div>

  <div class="person">
    <p><span class="person-name">Dr Marcus L. Avery</span> <span class="person-qual">BDSc (QLD)</span></p>
    <p class="person-title">Dental Surgeon, Clinical Director</p>
  </div>

  <ul class="contact">
    <li>(02) 9376 2258
      <svg viewBox="0 0 16 16"><path fill="#fff" d="M3 2h3l1 3-2 1a9 9 0 0 0 5 5l1-2 3 1v3a1 1 0 0 1-1 1A12 12 0 0 1 2 3a1 1 0 0 1 1-1z"/></svg>
    </li>
    <li>info@yoursmilekelvingrove.example.au
      <svg viewBox="0 0 16 16"><rect x="1" y="3" width="14" height="10" rx="1" fill="#fff"/><path d="M1.5 3.8 8 9l6.5-5.2" fill="none" stroke="#6aab22" stroke-width="1.3"/></svg>
    </li>
    <li>/yoursmilekelvingrove <span class="social-box"></span></li>
    <li class="address">Shop 5/12-14</li>
    <li class="address">Langford Rd Kelvin Grove</li>
    <li class="motto">Quality dentistry you can trust</li>
  </ul>
</section>

</body>
</html>
```